label design for cannabis

label template 4"x5.5" for a Massachusetts cannabis beverage product. labels will be transparent and placed on a blue (pantone 306C) bag.
https://www.fravostones.com/

Target Market(s)

cannabis customers in MA, 21+

Industry/Entity Type

cannabis consumer product

Font styles to use
Other font styles liked:
• DIN

Colors
0094D4
00A9DD
6FCCEA
C7EBF8
E9F6FB

Requirements
Must have
• label design with fravo logo, flavor (lemon, lime, plain, and coffee). 306C pantone for background and 11-0601 TCX for text. font=DINackground.
Nice to have
• tray icon, illustrated ice cubes in white (clear), yellow (lemon), green (lime) and brown (coffee)
Should not have
• no cartoonish characters

```html
<!DOCTYPE html>
<html lang="en">
<head>
<meta charset="utf-8">
<title>fravo infused ice cubes – flavour labels</title>
<link rel="stylesheet" href="https://fonts.googleapis.com/css2?family=Barlow+Condensed:wght@400;600&family=Barlow+Semi+Condensed:wght@700&display=swap">
<style>
  :root {
    --page: #dcdcdc;
    --label-blue: #0cb4e2;
    --text-white: #f4f4f2;
    --coffee: #9a4a1c;
    --lime: #b6d62a;
    --lemon: #f4e11c;
    --plain: #ffffff;
    --ink: #1b1b1b;
    --warn-red: #d8262c;
  }
  * { box-sizing: border-box; margin: 0; padding: 0; }
  html, body { width: 1200px; height: 655px; overflow: hidden; }
  body { background: var(--page); position: relative; }

  .label {
    position: absolute;
    top: 127px;
    width: 273px;
    height: 375px;
    background: var(--label-blue);
    color: var(--text-white);
  }
  .label--coffee { left: 39px; --flavour: var(--coffee); }
  .label--lime   { left: 331px; --flavour: var(--lime); }
  .label--lemon  { left: 622px; --flavour: var(--lemon); }
  .label--plain  { left: 914px; --flavour: var(--plain); }

  .brand-name {
    position: absolute;
    top: 30px;
    left: 0; right: 0;
    text-align: center;
    font-family: "Barlow Condensed", sans-serif;
    font-weight: 600;
    font-size: 116px;
    line-height: 1;
    letter-spacing: -1px;
    color: var(--text-white);
  }
  .product-line {
    position: absolute;
    top: 131px;
    left: 0; right: 0;
    text-align: center;
    font-family: "Barlow Condensed", sans-serif;
    font-weight: 400;
    font-size: 31px;
    line-height: 1;
    color: var(--text-white);
  }

  .flavour-art {
    position: absolute;
    top: 236px;
    left: 80px;
    width: 115px;
    height: 76px;
    border-radius: 38px;
  }
  .label--coffee .flavour-art { background: linear-gradient(90deg, #6e3414 0%, #9a5a2e 45%, #cfe9f6 75%, #8b4a20 100%); }
  .label--lime   .flavour-art { background: linear-gradient(90deg, #d6ec8a 0%, #8cc63e 45%, #d3ecf8 75%, #6aa832 100%); }
  .label--lemon  .flavour-art { background: linear-gradient(90deg, #f6e53a 0%, #f2c81e 50%, #d3ecf8 70%, #f0b81a 100%); }
  .label--plain  .flavour-art { left: 104px; width: 66px; border-radius: 14px; background: linear-gradient(135deg, #eaf7fd 0%, #b9e1f5 60%, #7cc6ea 100%); }

  .tray {
    position: absolute;
    top: 313px;
    left: 84px;
    width: 105px;
    height: 27px;
  }

  .flavour-name {
    position: absolute;
    top: 344px;
    left: 0; right: 0;
    text-align: center;
    font-family: "Barlow Semi Condensed", sans-serif;
    font-weight: 700;
    font-size: 15px;
    line-height: 1;
    color: var(--flavour);
  }
  .dose {
    position: absolute;
    top: 362px;
    left: 0; right: 0;
    text-align: center;
    font-family: "Barlow Semi Condensed", sans-serif;
    font-weight: 700;
    font-size: 7.5px;
    letter-spacing: 0.2px;
    line-height: 1;
    color: var(--text-white);
  }

  .warning-mark {
    position: absolute;
    top: 345px;
    left: 10px;
    width: 24px;
    height: 21px;
  }
  .kids-mark {
    position: absolute;
    top: 344px;
    left: 240px;
    width: 25px;
    height: 25px;
  }
</style>
</head>
<body>

<section class="label label--coffee">
  <h1 class="brand-name">fravo</h1>
  <p class="product-line">infused ice cubes</p>
  <div class="flavour-art" role="img" aria-label="Illustration of coffee beans with leaves and clear ice cubes"></div>
  <svg class="tray" viewBox="0 0 105 27" aria-hidden="true">
    <rect x="1" y="1" width="103" height="9" fill="none" stroke="var(--flavour)" stroke-width="2"/>
    <g fill="none" stroke="var(--flavour)" stroke-width="2">
      <path d="M3 10 L6 26 H16 L19 10"/><path d="M20 10 L23 26 H33 L36 10"/><path d="M37 10 L40 26 H50 L53 10"/>
      <path d="M54 10 L57 26 H67 L70 10"/><path d="M71 10 L74 26 H84 L87 10"/><path d="M88 10 L91 26 H101 L102 10"/>
    </g>
  </svg>
  <p class="flavour-name">coffee</p>
  <p class="dose">50MG PER TRAY</p>
  <svg class="warning-mark" viewBox="0 0 24 21" aria-hidden="true"><path d="M12 1 L23 20 H1 Z" fill="#fff" stroke="var(--warn-red)" stroke-width="2"/></svg>
  <svg class="kids-mark" viewBox="0 0 25 25" aria-hidden="true"><path d="M8 1 H17 L24 8 V17 L17 24 H8 L1 17 V8 Z" fill="#fff" stroke="var(--warn-red)" stroke-width="2"/></svg>
</section>

<section class="label label--lime">
  <h1 class="brand-name">fravo</h1>
  <p class="product-line">infused ice cubes</p>
  <div class="flavour-art" role="img" aria-label="Illustration of a whole lime and a lime slice with clear ice cubes"></div>
  <svg class="tray" viewBox="0 0 105 27" aria-hidden="true">
    <rect x="1" y="1" width="103" height="9" fill="none" stroke="var(--flavour)" stroke-width="2"/>
    <g fill="none" stroke="var(--flavour)" stroke-width="2">
      <path d="M3 10 L6 26 H16 L19 10"/><path d="M20 10 L23 26 H33 L36 10"/><path d="M37 10 L40 26 H50 L53 10"/>
      <path d="M54 10 L57 26 H67 L70 10"/><path d="M71 10 L74 26 H84 L87 10"/><path d="M88 10 L91 26 H101 L102 10"/>
    </g>
  </svg>
  <p class="flavour-name">lime</p>
  <p class="dose">50MG PER TRAY</p>
  <svg class="warning-mark" viewBox="0 0 24 21" aria-hidden="true"><path d="M12 1 L23 20 H1 Z" fill="#fff" stroke="var(--warn-red)" stroke-width="2"/></svg>
  <svg class="kids-mark" viewBox="0 0 25 25" aria-hidden="true"><path d="M8 1 H17 L24 8 V17 L17 24 H8 L1 17 V8 Z" fill="#fff" stroke="var(--warn-red)" stroke-width="2"/></svg>
</section>

<section class="label label--lemon">
  <h1 class="brand-name">fravo</h1>
  <p class="product-line">infused ice cubes</p>
  <div class="flavour-art" role="img" aria-label="Illustration of a lemon and a lemon half with clear ice cubes"></div>
  <svg class="tray" viewBox="0 0 105 27" aria-hidden="true">
    <rect x="1" y="1" width="103" height="9" fill="none" stroke="var(--flavour)" stroke-width="2"/>
    <g fill="none" stroke="var(--flavour)" stroke-width="2">
      <path d="M3 10 L6 26 H16 L19 10"/><path d="M20 10 L23 26 H33 L36 10"/><path d="M37 10 L40 26 H50 L53 10"/>
      <path d="M54 10 L57 26 H67 L70 10"/><path d="M71 10 L74 26 H84 L87 10"/><path d="M88 10 L91 26 H101 L102 10"/>
    </g>
  </svg>
  <p class="flavour-name">lemon</p>
  <p class="dose">50MG PER TRAY</p>
  <svg class="warning-mark" viewBox="0 0 24 21" aria-hidden="true"><path d="M12 1 L23 20 H1 Z" fill="#fff" stroke="var(--warn-red)" stroke-width="2"/></svg>
  <svg class="kids-mark" viewBox="0 0 25 25" aria-hidden="true"><path d="M8 1 H17 L24 8 V17 L17 24 H8 L1 17 V8 Z" fill="#fff" stroke="var(--warn-red)" stroke-width="2"/></svg>
</section>

<section class="label label--plain">
  <h1 class="brand-name">fravo</h1>
  <p class="product-line">infused ice cubes</p>
  <div class="flavour-art" role="img" aria-label="Illustration of three clear ice cubes"></div>
  <svg class="tray" viewBox="0 0 105 27" aria-hidden="true">
    <rect x="1" y="1" width="103" height="9" fill="none" stroke="var(--flavour)" stroke-width="2"/>
    <g fill="none" stroke="var(--flavour)" stroke-width="2">
      <path d="M3 10 L6 26 H16 L19 10"/><path d="M20 10 L23 26 H33 L36 10"/><path d="M37 10 L40 26 H50 L53 10"/>
      <path d="M54 10 L57 26 H67 L70 10"/><path d="M71 10 L74 26 H84 L87 10"/><path d="M88 10 L91 26 H101 L102 10"/>
    </g>
  </svg>
  <p class="flavour-name">plain</p>
  <p class="dose">50MG PER TRAY</p>
  <svg class="warning-mark" viewBox="0 0 24 21" aria-hidden="true"><path d="M12 1 L23 20 H1 Z" fill="#fff" stroke="var(--warn-red)" stroke-width="2"/></svg>
  <svg class="kids-mark" viewBox="0 0 25 25" aria-hidden="true"><path d="M8 1 H17 L24 8 V17 L17 24 H8 L1 17 V8 Z" fill="#fff" stroke="var(--warn-red)" stroke-width="2"/></svg>
</section>

</body>
</html>
```